Effectively Manage Muscular Pain /with Remedial Massage

A flyer to sell remedial massage Therapy for muscular pain .

$10 Discount with this flyer

Use colors orange and Blak with the color of the logo provided and preferably the fonts as well .

Little spin about remedial massage:

Remedial massage is a deep massage , to create the conditions for the body’s return to normal health after injury or with muscular-skeletal disorders. It is used to treat chronic muscular-skeletal imbalances, strains, sprains, broken bones, bruising or any injury. Deep tissue massage removes blockages, damaged cells, scar tissue and adhesions [speeds up recovery Remedial massage is also used for conditions created by lifestyle for example Repetitive strain injury and Back pain.

Target Market(s)

young professionals with kids , modern suburban couples

Industry/Entity Type

Massage

Requirements
Must have
• doble sided.

Address 418 kelvinhurst Rd , Footscray Book Now 94620387

```html
<!DOCTYPE html>
<html lang="en">
<head>
<meta charset="utf-8">
<title>Remedial Massage Flyer</title>
<link rel="stylesheet" href="https://fonts.googleapis.com/css2?family=Anton&family=Oswald:wght@400;500&family=Open+Sans:wght@400;600&display=swap">
<style>
  :root {
    --orange: #f05a22;
    --orange-deep: #d9481a;
    --black: #111114;
    --navy-black: #1a1a24;
    --grey-band: #8e8f93;
    --grey-band-dark: #7c7d81;
    --paper: #f2f2f2;
    --white: #ffffff;
    --bg: #ffffff;
  }
  * { box-sizing: border-box; margin: 0; padding: 0; }
  html, body { width: 1200px; height: 1184px; overflow: hidden; background: var(--bg); }
  body { position: relative; font-family: "Open Sans", Arial, sans-serif; }

  .flyer {
    position: absolute; top: 150px; width: 520px; height: 870px;
    background: linear-gradient(#ffffff, #e9e9ea 70%, #f5f5f5);
    box-shadow: 0 4px 18px rgba(0,0,0,.25);
    overflow: hidden;
  }
  .flyer--front { left: 50px; }
  .flyer--back { left: 630px; }

  /* Front */
  .header {
    height: 205px; background: var(--black);
    display: flex; align-items: center; padding: 0 30px; gap: 22px;
  }
  .brand-dot { width: 120px; height: 120px; border-radius: 50%; background: var(--orange); flex: none; }
  .brand-text {
    color: var(--white); font-family: "Oswald", sans-serif; font-size: 32px;
    line-height: 1.15; letter-spacing: .5px; white-space: nowrap;
  }
  .address-band {
    height: 34px; background: var(--orange); color: var(--black);
    font-family: "Oswald", sans-serif; font-weight: 500; font-size: 22px;
    text-align: right; padding-right: 30px; line-height: 34px;
  }
  .front-heading { position: relative; z-index: 2; }
  .front-title {
    text-align: center; font-family: "Anton", sans-serif; color: var(--orange);
    font-size: 50px; line-height: 1.1; margin-top: 12px; letter-spacing: .5px;
  }
  .front-sub { text-align: center; color: var(--orange); font-size: 22px; line-height: 1.2; }
  .front-photo {
    position: absolute; left: 0; right: 0; top: 350px; height: 330px; z-index: 1;
    background: radial-gradient(ellipse at 45% 55%, #f3c4c0 0%, #d9d9da 35%, #f0f0f0 75%);
  }

  .coupon {
    position: absolute; left: 50px; right: 40px; height: 125px; z-index: 2;
    background: linear-gradient(#22222c, var(--navy-black));
    border: 3px dashed var(--orange); border-radius: 14px;
    display: flex; align-items: center;
  }
  .flyer--front .coupon { top: 700px; }
  .flyer--back .coupon { top: 715px; }
  .coupon-offer { width: 46%; text-align: center; color: var(--white); border-right: 1px solid #555; }
  .coupon-amount { font-family: "Anton", sans-serif; color: var(--orange); font-size: 60px; line-height: 1; }
  .coupon-amount small { font-size: 30px; }
  .coupon-note { font-size: 21px; }
  .coupon-brand { flex: 1; padding-left: 16px; }
  .coupon-brand-row { display: flex; align-items: center; gap: 10px; }
  .coupon-dot { width: 46px; height: 46px; border-radius: 50%; background: var(--orange); flex: none; }
  .coupon-name { color: var(--white); font-family: "Oswald", sans-serif; font-size: 17px; line-height: 1.15; }
  .coupon-service { color: var(--orange); font-size: 14px; text-align: center; margin-top: 8px; line-height: 1.25; }

  /* Back */
  .back-photo {
    position: absolute; left: 0; top: 0; width: 190px; height: 230px;
    background: linear-gradient(160deg, #c9a27f 0%, #e7cbb4 40%, #9cb5d4 100%);
  }
  .pain-banner {
    position: absolute; left: 150px; right: 0; top: 70px; height: 120px;
    background: var(--orange); text-align: center; padding: 8px 0 0 40px;
  }
  .pain-title { font-family: "Anton", sans-serif; font-size: 42px; color: var(--black); line-height: 1.1; }
  .pain-sub { color: var(--white); font-size: 17px; line-height: 1.25; }
  .back-intro {
    position: absolute; left: 30px; right: 30px; top: 240px;
    color: var(--orange); text-align: center; font-size: 16px; font-weight: 600; line-height: 1.35;
  }
  .benefit-band {
    position: absolute; left: 0; right: 0; background: var(--grey-band);
    color: var(--white); text-align: center; font-size: 17px; line-height: 1.3;
    display: flex; align-items: center; justify-content: center; padding: 0 40px;
  }
  .band-2 { background: var(--grey-band-dark); }
  .benefit-arrow { position: absolute; top: -2px; left: 50%; transform: translateX(-50%); }
  .band-1 { top: 330px; height: 72px; }
  .band-2 { top: 406px; height: 52px; }
  .band-3 { top: 462px; height: 120px; }
  .discount-title {
    position: absolute; left: 0; right: 0; top: 600px; text-align: center;
    font-family: "Anton", sans-serif; color: var(--orange); font-size: 44px; line-height: 1.2;
  }
</style>
</head>
<body>

<section class="flyer flyer--front">
  <header class="header">
    <div class="brand-dot"></div>
    <div class="brand-text">MARLOW OSTEOPATHY<br>CLINICAL PILATES</div>
  </header>
  <div class="address-band">418 kelvinhurst Rd , Footscray</div>
  <div class="front-heading">
    <h1 class="front-title">Remedial Massage</h1>
    <p class="front-sub">for that pesky back pain</p>
  </div>
  <div class="front-photo" role="img" aria-label="Photo of a hand pressing on a painful lower back"></div>

  <div class="coupon">
    <div class="coupon-offer">
      <div class="coupon-amount">$10<small>off</small></div>
      <div class="coupon-note">with this flyer</div>
    </div>
    <div class="coupon-brand">
      <div class="coupon-brand-row">
        <div class="coupon-dot"></div>
        <div class="coupon-name">MARLOW OSTEOPATHY<br>CLINICAL PILATES</div>
      </div>
      <div class="coupon-service">Remedial Massage Therapy<br>for muscular pain</div>
    </div>
  </div>
</section>

<section class="flyer flyer--back">
  <div class="pain-banner">
    <h2 class="pain-title">Relief from PAIN</h2>
    <p class="pain-sub">strains, sprains, broken bones,<br>bruising or any injury</p>
  </div>
  <div class="back-photo" role="img" aria-label="Photo of a woman holding her sore neck"></div>
  <p class="back-intro">Remedial massage is a deep massage , to create the conditions for the body’s return to normal health after injury or with muscular-skeletal disorders.</p>

  <div class="benefit-band band-1">
    <svg class="benefit-arrow" width="18" height="12" viewBox="0 0 18 12"><path d="M0 0h18L9 12z" fill="#f05a22"/></svg>
    Removes blockages, damaged cells, scar tissue and adhesions
  </div>
  <div class="benefit-band band-2">
    <svg class="benefit-arrow" width="18" height="12" viewBox="0 0 18 12"><path d="M0 0h18L9 12z" fill="#f05a22"/></svg>
    Speeds up recovery
  </div>
  <div class="benefit-band band-3">
    <svg class="benefit-arrow" width="18" height="12" viewBox="0 0 18 12"><path d="M0 0h18L9 12z" fill="#f05a22"/></svg>
    Remedial massage is also used for conditions created by lifestyle for example repetitive strain injury and Back pain.
  </div>

  <h2 class="discount-title">Avail Discount TODAY!</h2>

  <div class="coupon">
    <div class="coupon-offer">
      <div class="coupon-amount">$10<small>off</small></div>
      <div class="coupon-note">with this flyer</div>
    </div>
    <div class="coupon-brand">
      <div class="coupon-brand-row">
        <div class="coupon-dot"></div>
        <div class="coupon-name">MARLOW OSTEOPATHY<br>CLINICAL PILATES</div>
      </div>
      <div class="coupon-service">Remedial Massage Therapy<br>for muscular pain</div>
    </div>
  </div>
</section>

</body>
</html>
```